Fresh Compass Guide - Life coaching program for young people

Life coaching program for young people, A 4 triple fold like it to bright and fun with headings on each page
Front page photo of young people in a life coaching program with company logo , inside first The Program 2nd page What is Life Coaching
3rd Page About Your Life Coach
Outside 1st Page Testimonials 2nd outside page contact page 3 page Title page

Target Market(s)

Young People. Parents and Schools

Industry/Entity Type

Life Coaching

Font styles to use
Serif

Colors
0255a3
3276b5
85acd3
edf2f7
cee9f5

Requirements
Must have
• Lots of colour and be fun to look at but professional
Nice to have
• Fun Graphic headings good use of photos
• would like to focus on design then put in the words to fit area put aside for information
Should not have
• too many words

```html
<!DOCTYPE html>
<html lang="en">
<head>
<meta charset="utf-8">
<title>Fresh Compass Guide – Brochure</title>
<link rel="stylesheet" href="https://fonts.googleapis.com/css2?family=Merriweather:wght@400;700;900&display=swap">
<style>
  :root{
    --blue:#213f91;
    --red:#d42a23;
    --navy:#34307a;
    --white:#ffffff;
    --ink:#2a2a2a;
    --rule:#333333;
    --page:#eef1f5;
  }
  *{box-sizing:border-box;margin:0;padding:0}
  html,body{width:1200px;height:866px;overflow:hidden;background:var(--page)}
  body{font-family:"Merriweather",Georgia,serif;color:var(--ink)}
  .brochure{position:relative;width:1200px;height:866px;display:grid;
    grid-template-columns:400px 400px 400px;grid-template-rows:482px 384px}
  .panel{position:relative;overflow:hidden}
  .photo{position:absolute}

  /* testimonials */
  .testimonials{background:var(--blue);color:var(--white);padding:26px 24px 0 58px}
  .testimonials h2{font-weight:900;font-size:30px;margin-left:-36px;margin-bottom:34px;letter-spacing:.3px}
  .quote{margin-bottom:28px}
  .quote p{font-size:13.2px;font-weight:700;line-height:20px;text-align:justify;word-spacing:2px}
  .quote cite{display:block;text-align:right;font-style:normal;font-size:12.5px;font-weight:700;margin-top:2px}

  /* kids with frames + call bar */
  .kids-photo{inset:0;background:linear-gradient(135deg,#c9b8a4 0%,#8f7a68 45%,#3d3a3e 80%,#22202a 100%)}
  .call-bar{position:absolute;background:var(--red);color:var(--white);font-weight:700;display:flex;align-items:center}
  .call-bar svg{flex:none}
  .call-left{left:146px;right:0;bottom:0;height:66px;padding-left:14px;gap:8px;font-size:21px;line-height:27px}
  .call-right{left:0;right:0;bottom:0;height:66px;justify-content:center;gap:10px;font-size:24px}

  /* centre top */
  .class-photo{left:0;top:0;width:400px;height:250px;background:linear-gradient(160deg,#b7a68f 0%,#6e7fb0 40%,#2f4f98 70%,#9c8b78 100%)}
  .mission{position:absolute;left:0;top:250px;width:400px;height:232px;background:var(--red);color:var(--white);
    display:flex;align-items:flex-end;justify-content:center;padding:0 30px 64px}
  .mission p{font-weight:700;font-size:17px;line-height:25px;text-align:center}

  /* contact */
  .contact{background:var(--white);padding:26px 34px 0 34px}
  .brand{display:flex;align-items:center;gap:12px;color:var(--navy);font-weight:700}
  .brand .dot{width:22px;height:22px;border-radius:50%;background:var(--red);flex:none}
  .contact .brand{justify-content:center;font-size:30px;line-height:36px;height:112px}
  .contact hr{border:0;border-top:2px solid var(--rule);margin:6px 0 22px}
  .contact ul{list-style:none;font-size:12.5px;line-height:21px}
  .contact li{display:flex;gap:12px;margin-bottom:9px;align-items:flex-start}
  .contact li svg{flex:none;margin-top:3px}
  .follow{display:flex;align-items:center;gap:6px;font-size:12.5px;margin-top:2px}
  .follow .badge{width:17px;height:17px;border-radius:3px;background:#4d7fc2}
  .follow span:first-child{margin-right:10px}

  /* title page */
  .title-page{grid-row:1 / span 2;grid-column:3;background:var(--white)}
  .title-band{position:absolute;left:0;top:0;width:400px;height:55px;background:var(--blue)}
  .title-page .brand{position:absolute;left:36px;top:108px;font-size:34px;line-height:42px;width:340px}
  .title-page .brand .dot{width:26px;height:26px}
  .headline{position:absolute;left:20px;right:20px;top:276px;color:var(--red);font-weight:700;font-size:29px;line-height:43px;text-align:center}
  .circle-photo{left:0;top:474px;width:400px;height:326px;background:linear-gradient(170deg,#e6e0d2 0%,#a9a6a0 35%,#6b6e76 65%,#3e6f78 100%)}
</style>
</head>
<body>
<main class="brochure">

  <section class="panel testimonials">
    <h2>Testimonials</h2>
    <blockquote class="quote">
      <p>“ Lorem Ispum is the dummy text of the Industry Lorem is the lore dummy lorem of the idselt ”</p>
      <cite>- Lorem Ispum</cite>
    </blockquote>
    <blockquote class="quote">
      <p>“ Lorem Ispum is the dummy text of the Industry Lorem is the lore dummy lorem of the idselt ”</p>
      <cite>- Lorem Ispum</cite>
    </blockquote>
    <blockquote class="quote">
      <p>“ Lorem Ispum is the dummy text of the Industry Lorem is the lore dummy lorem of the idselt ”</p>
      <cite>- Lorem Ispum</cite>
    </blockquote>
  </section>

  <section class="panel program-intro">
    <div class="photo class-photo" role="img" aria-label="Photo of a coach standing with a group of smiling students holding certificates in a classroom"></div>
    <div class="mission">
      <p>Lorem Ispum is the dummy text of the Industry Lorem is the lore dummy lorem of the idselt</p>
    </div>
  </section>

  <section class="panel title-page">
    <div class="title-band"></div>
    <div class="brand"><span class="dot"></span><span>Fresh Compass Guide</span></div>
    <h1 class="headline">Lorem Ispum is the dummy text of the Industry</h1>
    <div class="photo circle-photo" role="img" aria-label="Photo of young people seated in a circle during a coaching session"></div>
    <div class="call-bar call-right">
      <svg width="22" height="36" viewBox="0 0 22 36"><path d="M8 2c-4 1-6 4-6 9 0 7 3 15 8 21 2 2 5 3 8 1l2-2-4-6-3 2c-3-4-5-10-5-15l3-1-1-7z" fill="none" stroke="#fff" stroke-width="2.6" stroke-linejoin="round"/></svg>
      <span>Call Us Today 123 456 7890</span>
    </div>
  </section>

  <section class="panel coach-photo">
    <div class="photo kids-photo" role="img" aria-label="Photo of a smiling coach holding an award beside students showing framed posters"></div>
    <div class="call-bar call-left">
      <svg width="22" height="44" viewBox="0 0 22 44"><path d="M8 4c-4 1-6 5-6 11 0 8 3 17 8 24 2 2 5 3 8 1l2-2-4-7-3 2c-3-5-5-12-5-18l3-1-1-8z" fill="none" stroke="#fff" stroke-width="2.6" stroke-linejoin="round"/></svg>
      <span>Call Us Today<br>123 456 7890</span>
    </div>
  </section>

  <section class="panel contact">
    <div class="brand"><span class="dot"></span><span>Fresh Compass Guide</span></div>
    <hr>
    <ul>
      <li>
        <svg width="14" height="16" viewBox="0 0 14 16"><path d="M7 15s5-5 5-9A5 5 0 0 0 2 6c0 4 5 9 5 9z" fill="#222"/><circle cx="7" cy="6" r="2" fill="#fff"/></svg>
        <span>Street name, State Name<br>State Zip Code</span>
      </li>
      <li>
        <svg width="16" height="12" viewBox="0 0 16 12"><rect x="0.5" y="0.5" width="15" height="11" fill="#222"/><path d="M1 1l7 6 7-6" fill="none" stroke="#fff" stroke-width="1.2"/></svg>
        <span>hello@freshcompassguide.com</span>
      </li>
      <li>
        <svg width="15" height="15" viewBox="0 0 15 15"><circle cx="7.5" cy="7.5" r="6.5" fill="none" stroke="#555" stroke-width="1.2"/><path d="M1 7.5h13M7.5 1v13M3 3.5c3 2 6 2 9 0M3 11.5c3-2 6-2 9 0" fill="none" stroke="#555" stroke-width="1"/></svg>
        <span>www.freshcompassguide.com</span>
      </li>
      <li>
        <svg width="14" height="16" viewBox="0 0 14 16"><path d="M5 1C2 2 1 4 1 7c0 3 2 7 5 8 1 1 3 0 4-1l-2-3-2 1C5 10 4 8 4 6l2-1-1-4z" fill="#222"/></svg>
        <span>123 456 7890</span>
      </li>
      <li>
        <svg width="15" height="15" viewBox="0 0 15 15"><rect x="3" y="1" width="9" height="4" fill="#222"/><rect x="1" y="6" width="13" height="6" fill="#222"/><rect x="4" y="10" width="7" height="4" fill="#fff" stroke="#222"/></svg>
        <span>123 456 7890</span>
      </li>
    </ul>
    <div class="follow"><span>Follow us on</span><span class="badge"></span><span class="badge"></span><span class="badge"></span></div>
  </section>

</main>
</body>
</html>
```